Marrowby's Vacation Rentals Business Card

Multi Million dollar villa rentals in the Dominican Republic.

Industry/Entity Type

Business

Contact Information for Business Card

I am looking for a high-end look around my company name/logo (see attached) on one side incorporating the following info: first and last name, title, address, phone #, email and company website. On the backside I want to add a full color picture of one of our villas (see attached).

```html
<!DOCTYPE html>
<html lang="en">
<head>
<meta charset="utf-8">
<title>Marrowby's Vacation Rentals Business Card</title>
<link href="https://fonts.googleapis.com/css2?family=Open+Sans:wght@400;600;700&display=swap" rel="stylesheet">
<style>
  :root {
    --backdrop: #e6e8eb;
    --card: #ffffff;
    --ink: #1d1d1d;
    --ink-soft: #5a5a5a;
    --accent: #f07a2a;
    --sky: #8fb8dc;
    --villa: #e9e4dc;
    --pool: #2f8fd0;
  }
  * { margin: 0; padding: 0; box-sizing: border-box; }
  html, body { width: 1200px; height: 952px; overflow: hidden; }
  body {
    background: var(--backdrop);
    font-family: "Open Sans", Arial, sans-serif;
    color: var(--ink);
    display: flex;
    flex-direction: column;
    align-items: center;
    justify-content: center;
    gap: 40px;
  }
  .card {
    position: relative;
    width: 720px;
    height: 412px;
    background: var(--card);
    box-shadow: 0 6px 20px rgba(0,0,0,0.12);
    overflow: hidden;
  }
  .brand {
    display: flex;
    align-items: center;
    gap: 14px;
  }
  .brand-dot {
    width: 46px; height: 46px;
    border-radius: 50%;
    background: var(--accent);
    flex: none;
  }
  .brand-name {
    font-weight: 600;
    color: var(--ink);
    line-height: 1.05;
  }
  .brand-name .line-1 { display: block; font-size: 38px; }
  .brand-name .line-2 { display: block; font-size: 20px; letter-spacing: 3px; text-transform: uppercase; }

  /* front */
  .card-front .brand { position: absolute; left: 40px; bottom: 44px; }
  .contact {
    position: absolute;
    left: 400px;
    top: 92px;
  }
  .contact .person { font-size: 32px; color: var(--ink-soft); font-weight: 400; line-height: 1.1; }
  .contact .person strong { font-weight: 700; }
  .contact .job { font-size: 20px; color: var(--accent); margin-top: 4px; margin-bottom: 22px; }
  .contact ul { list-style: none; }
  .contact li {
    display: flex; align-items: center; gap: 14px;
    font-size: 18px; color: var(--ink-soft);
    margin-bottom: 12px;
  }
  .contact svg { width: 18px; height: 18px; fill: var(--accent); flex: none; }

  /* back */
  .villa-photo {
    position: absolute; left: 0; top: 0;
    width: 100%; height: 300px;
    background: linear-gradient(180deg, var(--sky) 0%, var(--villa) 38%, var(--villa) 70%, var(--pool) 100%);
  }
  .card-back .brand { position: absolute; left: 40px; bottom: 22px; }
  .card-back .website {
    position: absolute; right: 46px; bottom: 40px;
    font-size: 20px; font-weight: 600; color: var(--ink);
  }
</style>
</head>
<body>
  <section class="card card-front">
    <div class="brand">
      <span class="brand-dot"></span>
      <span class="brand-name"><span class="line-1">Marrowby's</span><span class="line-2">Vacation Rentals</span></span>
    </div>
    <div class="contact">
      <p class="person">Your <strong>Name</strong></p>
      <p class="job">Job Title</p>
      <ul>
        <li><svg viewBox="0 0 24 24"><path d="M12 2a7 7 0 0 0-7 7c0 5 7 13 7 13s7-8 7-13a7 7 0 0 0-7-7zm0 9.5A2.5 2.5 0 1 1 12 6.5a2.5 2.5 0 0 1 0 5z"/></svg>Your Address</li>
        <li><svg viewBox="0 0 24 24"><path d="M3 8c0-2 4-4 9-4s9 2 9 4v2h-5V8H8v2H3zM6 12h12l2 8H4z"/></svg>000 000 0000</li>
        <li><svg viewBox="0 0 24 24"><path d="M2 5h20v14H2zm2 2v.5l8 5.5 8-5.5V7z"/></svg>youremail@xyz.com</li>
        <li><svg viewBox="0 0 24 24"><path d="M12 2a10 10 0 1 0 0 20 10 10 0 0 0 0-20zm0 2c1.5 1.8 2.4 4.5 2.6 7H9.4C9.6 8.5 10.5 5.8 12 4zm-2.6 9h5.2c-.2 2.5-1.1 5.2-2.6 7-1.5-1.8-2.4-4.5-2.6-7zM4.1 11a8 8 0 0 1 4.3-6.2A13 13 0 0 0 7.4 11zm0 2h3.3a13 13 0 0 0 1 6.2A8 8 0 0 1 4.1 13zm12.5 0h3.3a8 8 0 0 1-4.3 6.2 13 13 0 0 0 1-6.2zm0-2a13 13 0 0 0-1-6.2A8 8 0 0 1 19.9 11z"/></svg>www.yourwebsite.com</li>
      </ul>
    </div>
  </section>

  <section class="card card-back">
    <div class="villa-photo" role="img" aria-label="Photograph of a white villa with terracotta roof, balustraded terrace, palm trees and a blue swimming pool with lounge chairs"></div>
    <div class="brand">
      <span class="brand-dot"></span>
      <span class="brand-name"><span class="line-1">Marrowby's</span><span class="line-2">Vacation Rentals</span></span>
    </div>
    <p class="website">www.yourwebsite.com</p>
  </section>
</body>
</html>
```